Small environmental consultancy needs a simple but professional web design

We are a boutique environmental consultancyand contracting business located in Margaret River in the South West of Western Australia.

We have two arms
1) Consulting which offers environmental planning, management and assessment services primarily to local government and the development industry.
2) Contracting which implements on site plans and on ground works primarily involving revegetation, bush regeneration and environmental weed control.

We need a simple yet professional web design within the wordpress platform that commmunicates professionalism, experience and technical expertise without appearing too corporate.

Something like this structure appeals:
http://verdantia.net.au/environment-services/
or
http://www.ridgefallenvironmental.com.au/index.php

(without the image gallery function)

Target Market(s)

Local Government Officers deciding on tenders;
Developers, Engineers, Town Planning consultants looking for environmental expertise

Industry/Entity Type

Business

Number of Pages Required

5+ page

Font styles to use
Sans Serif

Colors
33a6d7
9bcb3c

Requirements
Must have
• Pages required include:
• Home
• Environmental Planning and Management
• Revegetation and Regeneration Implementation (This page can mirror the Environmental Planning and Management page exactly in structure but with different text and images)
• About Us (I think that this page can be relatively simple and generic)
• Contact (I think that this page can be very simple and generic)
Nice to have
• An ability to start out basic and quicikly establish a website presence and then build in additional drop downs and pages over time.
Should not have
• It does not need a photo gallery page;
• It does not need a major amount of space dedicated to social media and blogs etc as this is not currently particularly active area for us

```html
<!DOCTYPE html>
<html lang="en">
<head>
<meta charset="utf-8">
<title>Tarrena Ecoservices</title>
<link href="https://fonts.googleapis.com/css2?family=PT+Sans:wght@400;700&display=swap" rel="stylesheet">
<style>
  :root {
    --surround: #d6d7d9;
    --page: #ffffff;
    --ink: #2f3236;
    --body-text: #9a9a9a;
    --nav-text: #555555;
    --nav-active: #9a5a1e;
    --accent: #9bcb3c;
    --brand: #7a4f1f;
    --footer: #7a5122;
    --rule: #e6e6e6;
  }
  * { margin: 0; padding: 0; box-sizing: border-box; }
  html, body { width: 1200px; height: 1000px; overflow: hidden; }
  body {
    background: var(--surround);
    font-family: "PT Sans", Arial, sans-serif;
    position: relative;
  }
  .site {
    position: absolute; left: 113px; top: 0; width: 974px; height: 1000px;
    background: var(--page);
    box-shadow: 0 0 18px rgba(0,0,0,0.18);
  }
  .site-header { position: absolute; left: 0; top: 0; width: 100%; height: 62px; }
  .brand {
    position: absolute; left: 139px; top: 14px;
    display: flex; align-items: center; gap: 10px;
  }
  .brand-mark { width: 30px; height: 30px; border-radius: 50%; background: var(--accent); }
  .brand-name { font-size: 26px; font-weight: 400; color: var(--brand); line-height: 1; }
  .main-nav {
    position: absolute; left: 437px; top: 36px;
    display: flex; gap: 0; font-size: 7px; color: var(--nav-text);
  }
  .main-nav a { color: inherit; text-decoration: none; margin-right: 19px; }
  .main-nav a.active { color: var(--nav-active); margin-right: 26px; }
  .hero {
    position: absolute; left: 0; top: 62px; width: 100%; height: 318px;
    background: radial-gradient(ellipse 30% 55% at 50% 40%, #a9c98a 0%, #5d8a3a 35%, #2f4d1c 70%, #1a2a10 100%);
  }
  .section { position: absolute; left: 195px; width: 578px; }
  .section-title {
    font-size: 19px; font-weight: 700; color: var(--ink);
    padding-left: 13px; position: relative; line-height: 20px; text-transform: uppercase;
  }
  .section-title::before {
    content: ""; position: absolute; left: 0; top: 1px; width: 5px; height: 18px; background: var(--accent);
  }
  .welcome { top: 421px; }
  .welcome p { font-size: 8px; line-height: 13.5px; color: var(--body-text); }
  .welcome p:first-of-type { margin-top: 26px; }
  .welcome p + p { margin-top: 13px; }
  .divider { position: absolute; left: 0; top: 624px; width: 100%; height: 1px; background: var(--rule); }
  .projects { top: 664px; width: 585px; }
  .project-grid { display: flex; gap: 15px; margin-top: 31px; }
  .project { width: 185px; }
  .project-image { position: relative; width: 185px; height: 125px; }
  .project-image::after {
    content: ""; position: absolute; left: 0; bottom: 0; width: 25px; height: 25px; background: var(--accent);
  }
  .img-seedling { background: linear-gradient(160deg, #1a1a1a 0%, #3d3d3d 55%, #8a8a8a 100%); }
  .img-leaf { background: radial-gradient(circle at 50% 45%, #7ab23a 0%, #4f8a22 60%, #2f5a12 100%); }
  .img-tree { background: linear-gradient(180deg, #cfe0ee 0%, #a9d24a 45%, #6a9a2a 75%, #8ab55a 100%); }
  .project-title { margin-top: 10px; font-size: 9px; font-weight: 700; color: var(--ink); }
  .project p { margin-top: 4px; font-size: 8px; line-height: 13px; color: var(--body-text); }
  .site-footer {
    position: absolute; left: 0; top: 952px; width: 100%; height: 48px; background: var(--footer);
  }
  .copyright { position: absolute; left: 195px; top: 20px; font-size: 7px; color: #ffffff; }
  .social { position: absolute; left: 697px; top: 21px; display: flex; gap: 11px; }
  .social span { width: 7px; height: 7px; border-radius: 50%; background: #ffffff; }
</style>
</head>
<body>
<div class="site">
  <header class="site-header">
    <div class="brand">
      <span class="brand-mark"></span>
      <span class="brand-name">Tarrena Ecoservices</span>
    </div>
    <nav class="main-nav">
      <a href="#" class="active">Home</a>
      <a href="#">Environmental Planning and Management</a>
      <a href="#">Revegetation and Regeneration Implementation</a>
      <a href="#">About Us</a>
      <a href="#">Contact</a>
    </nav>
  </header>

  <div class="hero" role="img" aria-label="Photo of a misty green forest path under arching trees"></div>

  <section class="section welcome">
    <h2 class="section-title">Welcome</h2>
    <p>Lorem ipsum dolor sit amet, consectetur adipiscing elit. Sed nisi metus, tristique ndolor non, ornare sagittis dolor. Nulla vestibulu lacus sed molestie gravida. Crferm entum &nbsp;quismagna congue, vel sodales arcu vestibulum. Nunc lobortis dui magna, quis lacusullamcorper at.</p>
    <p>Phasellus sollicitudin ante eros ornare, sit amet luctus lorem semper. Suspendisse posuere, quamdictum consectetur, augue metus pharetra tellus, eu feugiatloreg egetnisi. Cras ornare bibendum ante, ut bibendum odio convallis eget. vel sodales arcu vestibulum.</p>
  </section>

  <div class="divider"></div>

  <section class="section projects">
    <h2 class="section-title">Recent Projects</h2>
    <div class="project-grid">
      <article class="project">
        <div class="project-image img-seedling" role="img" aria-label="Photo of cupped hands holding soil with a green seedling"></div>
        <h3 class="project-title">PROJECT 01</h3>
        <p>Integer vel lacus non dui ullamcorper venenatis. Aliquam vitae tristique nisi, vitae ullamcorper risus. Nam porttitor blandit ultricies.</p>
      </article>
      <article class="project">
        <div class="project-image img-leaf" role="img" aria-label="Close-up photo of a green leaf and its veins"></div>
        <h3 class="project-title">PROJECT 02</h3>
        <p>Integer vel lacus non dui ullamcorper venenatis. Aliquam vitae tristique nisi, vitae ullamcorper risus. Nam porttitor blandit ultricies.</p>
      </article>
      <article class="project">
        <div class="project-image img-tree" role="img" aria-label="Photo of a bright green tree standing in a grassy park"></div>
        <h3 class="project-title">PROJECT 03</h3>
        <p>Integer vel lacus non dui ullamcorper venenatis. Aliquam vitae tristique nisi, vitae ullamcorper risus. Nam porttitor blandit ultricies.</p>
      </article>
    </div>
  </section>

  <footer class="site-footer">
    <p class="copyright">© Copyright 2014 by Tarrena Ecoservices. All Rights Reserved.</p>
    <div class="social" aria-label="Social links">
      <span></span><span></span><span></span><span></span><span></span>
    </div>
  </footer>
</div>
</body>
</html>
```